A-Stand Directional Sign Design

Objective:
We need a professional graphic design for an A-Stand sign that will guide customers arriving in our parking lot to our office. The design should be visually clear, welcoming, and aligned with our brand identity.
REQUIREMENTS:
Two versions of the design:
- One with an arrow pointing left
- One with an arrow pointing right
(This allows us to place the A-Stand anywhere and flip the graphic as needed.)
DIMENSIONS:
- Viewable Area: 30" x 40"
BRAND ALIGNMENT:
- Colors, fonts, and overall style should match our website: www.skornabel.com
- Clean, modern, and professional look consistent with our aviation/tourism brand
CONTENT:
- Clear directional arrow (left or right depending on version)
- Text: “Office Entrance” or similar concise wording (designers may propose alternatives if they improve clarity)
READABILITY:
- Bold, high-contrast design for visibility from a distance
- Simple layout that avoids clutter
DELIVERABLES:
- Final artwork in print-ready format (PDF preferred)
- Two versions: Arrow Left and Arrow Right
DESIGN GOAL:
Ensure customers can easily find our office upon arrival, while reinforcing skorNABEL’s professional and welcoming brand image.
Target Market(s)
Tourism

```html
<!DOCTYPE html>
<html lang="en">
<head>
<meta charset="utf-8">
<title>skorNABEL – Office Entrance A-Stand</title>
<link href="https://fonts.googleapis.com/css2?family=Poppins:wght@500;600&display=swap" rel="stylesheet">
<style>
  :root {
    --backdrop: #777777;
    --sign-white: #ffffff;
    --ink-dark: #2e2e2e;
    --brand-blue: #227bbf;
    --photo-warm: #7a5a48;
    --photo-mid: #b9a494;
    --photo-light: #e9e7e5;
    --logo-white: #ffffff;
  }
  html, body {
    margin: 0;
    padding: 0;
    width: 1200px;
    height: 1200px;
    overflow: hidden;
    background: var(--backdrop);
  }
  .sign {
    position: absolute;
    left: 75px;
    top: 168px;
    width: 1050px;
    height: 787px;
    background: var(--sign-white);
    overflow: hidden;
  }
  .sign__photo {
    position: absolute;
    left: 0;
    top: 0;
    width: 1050px;
    height: 372px;
    background: linear-gradient(100deg, var(--photo-warm) 0%, var(--photo-mid) 45%, var(--photo-light) 100%);
  }
  .sign__brand {
    position: absolute;
    left: 105px;
    top: 110px;
    font-family: "Poppins", sans-serif;
    font-weight: 600;
    font-size: 38px;
    letter-spacing: 1px;
    color: var(--logo-white);
    margin: 0;
    line-height: 1;
  }
  .sign__title {
    position: absolute;
    left: 202px;
    top: 356px;
    margin: 0;
    font-family: "Poppins", sans-serif;
    font-weight: 500;
    font-size: 206px;
    line-height: 1.2;
    letter-spacing: -2px;
    color: var(--ink-dark);
  }
  .sign__subtitle {
    position: absolute;
    left: 208px;
    top: 636px;
    margin: 0;
    font-family: "Poppins", sans-serif;
    font-weight: 500;
    font-size: 58px;
    line-height: 1.2;
    color: var(--brand-blue);
  }
  .sign__arrow {
    position: absolute;
    left: 487px;
    top: 610px;
  }
</style>
</head>
<body>
  <main class="sign">
    <div class="sign__photo" role="img" aria-label="Photo of smiling passengers wearing aviation headsets inside a helicopter cabin"></div>
    <p class="sign__brand">skorNABEL</p>
    <h1 class="sign__title">Office</h1>
    <p class="sign__subtitle">Entrance</p>
    <svg class="sign__arrow" width="420" height="120" viewBox="0 0 420 120" aria-hidden="true">
      <polygon points="0,32 314,32 314,0 411,57 314,114 314,84 0,84" fill="var(--brand-blue)"/>
    </svg>
  </main>
</body>
</html>
```